Tending Our Garden eBook Cover Design

I want to deisgn a cover for my eBook (FRONT COVER) and the title is:

What I Grew From a Single Spark. And Why It Matters
By KT Dorran

TITLE CHANGED TO: UNDER THE WILLOW TREE; WHERE I FOUND MY QUIET STRENGTH AND WHERE YOU MIGHT TOO

The color palette is attached. Along with some photos options of me. Along with the ebook in WORD Document. My website is www.KTDorranLive.example. You can use a different color palette if you think it is best

Target Market(s)

women who look to build a personal brand

Industry/Entity Type

health and wellness

Requirements
Must have
• the title
Nice to have
• use my picture on the cover; but that is optional
Should not have
• any men

```html
<!DOCTYPE html>
<html lang="en">
<head>
<meta charset="utf-8">
<title>Under the Willow Tree — KT Dorran</title>
<link href="https://fonts.googleapis.com/css2?family=Barlow+Condensed:wght@600&family=Mrs+Saint+Delafield&display=swap" rel="stylesheet">
<style>
  :root {
    --stage: #d4d4d4;
    --cover: #050505;
    --rose: #d8aca2;
    --white: #ffffff;
    --dress: #e8361c;
    --dress-deep: #b6260f;
    --hair: #0d0b0a;
  }
  * { margin: 0; padding: 0; box-sizing: border-box; }
  html, body {
    width: 1200px;
    height: 1200px;
    overflow: hidden;
    background: var(--stage);
  }
  .cover {
    position: absolute;
    left: 220px;
    top: 24px;
    width: 760px;
    height: 1152px;
    background: var(--cover);
    overflow: hidden;
    box-shadow: 0 10px 30px rgba(0,0,0,0.25);
  }
  .cover__portrait {
    position: absolute;
    left: 344px;
    top: 468px;
    width: 416px;
    height: 684px;
  }
  .cover__title {
    position: absolute;
    left: 62px;
    top: 44px;
    font-family: "Barlow Condensed", "Arial Narrow", sans-serif;
    font-weight: 600;
    font-size: 96px;
    line-height: 0.95;
    letter-spacing: 0.5px;
    text-transform: uppercase;
    color: var(--rose);
  }
  .cover__title .accent { color: var(--white); }
  .cover__author {
    position: absolute;
    left: 70px;
    top: 900px;
    font-family: "Mrs Saint Delafield", cursive;
    font-size: 128px;
    line-height: 1;
    color: var(--white);
    transform: rotate(-8deg);
    transform-origin: left bottom;
    white-space: nowrap;
  }
</style>
</head>
<body>
  <main class="cover">
    <svg class="cover__portrait" viewBox="0 0 416 684" role="img" aria-label="Portrait of the author in a red dress, seated on a wooden director's chair">
      <defs>
        <linearGradient id="portraitTone" x1="0" y1="0" x2="0" y2="1">
          <stop offset="0" stop-color="var(--hair)"/>
          <stop offset="0.3" stop-color="#2a1a17"/>
          <stop offset="0.45" stop-color="var(--dress)"/>
          <stop offset="1" stop-color="var(--dress-deep)"/>
        </linearGradient>
      </defs>
      <rect width="416" height="684" fill="url(#portraitTone)"/>
    </svg>
    <h1 class="cover__title">
      Under the<br>
      Willow Tree;<br>
      Where I Found<br>
      My Quiet<br>
      Strength<br>
      And <span class="accent">Where</span><br>
      <span class="accent">You Might</span><br>
      <span class="accent">Too</span>
    </h1>
    <p class="cover__author">KT Dorran</p>
  </main>
</body>
</html>
```